Custom Header Designs - Automotive Parts - Alternator & Starter

We need 8 Header/Hero designs that will be used on our website. We are a company based in Montreal Canada and we re-manufacture Alternators and Starters for all types of vehicles. We offer a premium product and we are looking for premium designs that reflect the look of our packaging and the look of our website. Essentially we specialize in the sale and manufacture of two specific parts that go on all types of vehicles, Alternators and Starters. All text on these designs need to be editable as we will need to translate them to French once we get the source files.
Here are some websites of our competitors so you can draw some inspiration and see what our industry/business is all about:
https://www.qelvorparts.com/
https://www.zentrihaul.com/
Article that describes a remanufactured product, https://www.wombrixo.com/articles/starters-and-alternators-reman-vs-new.html
Our packaging is modern, sleek and professional. Our website is a B2B E-Commerce Site as well as an info site to promote our products. It is clean and minimal but we want the header/hero designs to help it stand out. Our main colors are blue and gray (as seen in our logo), but you can use whatever you like to compliment these colors.
Our packaging design was done on PixelTroupe, here is the link to that project so that you can see the packaging look and use any of the info that is from that project.
https://jobs.pixeltroupe.ca/job/5829463
The 8 Header/Hero designs will be used in the following areas, I have included a brief description of what we are looking for:
1 - Homepage Header/Hero image - This will be the homepage hero image therefore it should summarize the info described below. We offer premium quality re-manufactured alternators and starters. We are a wholesaler/distributor that services major auto-part stores with these quality products.
2 - General Product Header/Hero image - This image will be used as a header where the customer can learn general info about our products and any custom work we can do. This page will have a section where you can click to learn more about our individual product lines (links to product specific pages mentioned below) and a description of the custom work we can perform. We offer a two year manufacturers warranty.
3 - Alternator Product Header/Hero image - This image will be used to showcase our Alternator Product Line. Its purpose is to promote and advertise our premium re-manufactured alternators. This page will provide detailed info about our alternator re-manufacturing process and describe why our alternators are great.
4 - Starter Product Header/Hero image - This image will be used to showcase our Starter Product Line. Its purpose is to promote and advertise our premium re-manufactured starters. This page will provide detailed info about our starter re-manufacturing process and describe why our starters are great.
5 - General Header/Hero Image - This image will be used in most of our standard pages like our terms and conditions, privacy policy, warranty policy, our company page, etc. It needs to relate to the industry but be general enough so that we could use it in multiple areas
6 - Online Ordering Header image - This image will be used in our B2B area to introduce our customers to the Online Ordering system, its purpose is to advertise and explain some of the features of the Online Ordering system.
7 - B/O Re-Manufacture & Return Header Image - This image will be used in our B2B area to explain and advertise to our customers how our Backorder/R&R process works on our website. Essentially if we do not have the remanufactured part in stock but we have the core you could put the product on Backorder and we will remanufacture it in a few hours. If for any reason (rare vehicle, old vehicle, etc.) we do not have the core we will R&R (Remanufacture and Return) the customers core for them.
8 - Bulk Ordering Form Header Image - This image will be used in our B2B area to explain and advertise to our customers how our Bulk Ordering Form works on our website.
These hero/header images will be going on a Plankly/TillNest website and I am suggesting these images have a size of 1600 x 500, but we will take any other suggestions from the designers as you are the experts.
I have included a zip file that includes images of various elements that will help you in the design process.
Target Market(s)
Educate consumers about our products and attract auto supply chains to become distributors of our products.
Industry/Entity Type
Automotive Part

```html
<!DOCTYPE html>
<html lang="en">
<head>
<meta charset="utf-8">
<title>Ampora – Premium Auto Parts</title>
<link rel="stylesheet" href="https://fonts.googleapis.com/css2?family=Poppins:wght@500;600&family=Arimo:wght@400;700&display=swap">
<style>
  :root {
    --topbar-bg: #f2f2f2;
    --link-blue: #4a5aa8;
    --text-gray: #5a5a5a;
    --brand-blue: #2a3f8f;
    --navy-top: #0d2148;
    --navy-bottom: #020a1b;
    --stats-bg: #0a1c44;
    --headline: #d0d1d5;
    --white: #ffffff;
    --badge: #a9d3ec;
  }
  * { box-sizing: border-box; margin: 0; padding: 0; }
  html, body { width: 1200px; height: 794px; overflow: hidden; }
  body { font-family: "Arimo", Arial, sans-serif; background: var(--white); position: relative; }

  .topbar { position: absolute; left: 0; top: 0; width: 1200px; height: 29px; background: var(--topbar-bg); font-size: 12.5px; }
  .topbar span { position: absolute; top: 7px; white-space: nowrap; }
  .topbar .consult { left: 91px; color: var(--link-blue); }
  .topbar .call { left: 552px; color: #8a8a8a; }
  .topbar .call b { color: #333; letter-spacing: .3px; }
  .topbar .sep { left: 713px; color: #999; }
  .topbar .map { left: 731px; color: var(--link-blue); }
  .topbar .dashboard { left: 879px; top: 9px; font-size: 10px; color: var(--link-blue); letter-spacing: .2px; }
  .topbar .lang { left: 1034px; top: 8px; font-size: 10px; color: #555; }
  .lang .flag { display: inline-block; width: 15px; height: 10px; background: #2b3f8a; border: 1px solid #c8102e; vertical-align: -1px; margin-right: 2px; }

  .header { position: absolute; left: 0; top: 29px; width: 1200px; height: 90px; background: var(--white); }
  .brand { position: absolute; left: 104px; top: 26px; display: flex; align-items: center; gap: 10px; }
  .brand .mark { width: 34px; height: 34px; border-radius: 50%; background: var(--brand-blue); }
  .brand .name { font-family: "Poppins", sans-serif; font-weight: 600; font-size: 34px; color: var(--brand-blue); line-height: 1; }
  .nav { position: absolute; top: 34px; left: 0; font-size: 13.5px; color: var(--text-gray); }
  .nav span { position: absolute; white-space: nowrap; }
  .cart { position: absolute; left: 1071px; top: 34px; }
  .cart .badge { position: absolute; left: 20px; top: -10px; width: 17px; height: 17px; border-radius: 50%; background: var(--badge); color: var(--link-blue); font-size: 8px; text-align: center; line-height: 17px; }

  .hero { position: absolute; left: 0; top: 119px; width: 1200px; height: 675px; background: linear-gradient(180deg, #f4f4f5 0%, #d6d7da 45%, #8c8f95 100%); }
  .hero-panel { position: absolute; left: 0; top: 0; width: 829px; height: 675px; background: linear-gradient(180deg, var(--navy-top) 0%, #06142f 55%, var(--navy-bottom) 100%); overflow: hidden; }
  .hero-panel svg { position: absolute; left: 0; top: 0; }

  .headline { position: absolute; left: 85px; top: 140px; font-family: "Poppins", sans-serif; font-weight: 600; font-size: 42px; line-height: 44px; color: var(--headline); letter-spacing: .3px; }
  .lead { position: absolute; left: 88px; top: 251px; width: 440px; font-size: 15px; line-height: 21.5px; color: var(--white); }

  .stats { position: absolute; left: 86px; top: 348px; width: 472px; height: 123px; background: var(--stats-bg); border-radius: 10px; display: flex; }
  .stat { flex: 1; text-align: center; color: var(--white); padding-top: 18px; position: relative; }
  .stat + .stat::before { content: ""; position: absolute; left: 0; top: 18px; height: 89px; border-left: 1px solid #34476f; }
  .stat .num { font-family: "Arimo", sans-serif; font-weight: 700; font-size: 42px; line-height: 44px; }
  .stat .label { font-size: 13.5px; margin-top: 8px; line-height: 15px; }
  .stat .desc { font-size: 12px; line-height: 14px; }

  .cta { position: absolute; left: 88px; top: 519px; width: 222px; height: 47px; border-radius: 24px; background: linear-gradient(90deg, #c9cbcf 0%, #ffffff 35%, #f3f3f4 70%, #b9bbc0 100%); box-shadow: -2px 3px 0 #8b8e94; font-family: "Poppins", sans-serif; font-weight: 500; font-size: 14px; color: #1b2a4c; text-align: center; line-height: 47px; letter-spacing: .3px; }

  .hero-photo { position: absolute; left: 645px; top: 167px; width: 490px; height: 326px; background: linear-gradient(100deg, #a9c4d8 0%, #8e9b8f 22%, #45c2c7 55%, #3fc9cc 80%, #9aa3a8 100%); }
</style>
</head>
<body>
  <div class="topbar">
    <span class="consult">Book a Sales Consultation →</span>
    <span class="call">Call us now: <b>514.555.0182</b></span>
    <span class="sep">|</span>
    <span class="map">Find us on the map →</span>
    <span class="dashboard">MY AMPORA DASHBOARD</span>
    <span class="lang"><i class="flag"></i>English (English)</span>
  </div>

  <header class="header">
    <div class="brand"><span class="mark"></span><span class="name">Ampora</span></div>
    <nav class="nav">
      <span style="left:354px">Home</span>
      <span style="left:412px">Products</span>
      <span style="left:487px">Our Company</span>
      <span style="left:592px">Customer Resources</span>
      <span style="left:740px">Contact Us</span>
      <span style="left:829px">Online Ordering</span>
      <span style="left:945px">Hello, administrator</span>
    </nav>
    <div class="cart">
      <svg width="20" height="22" viewBox="0 0 20 22" fill="none" stroke="#333" stroke-width="1.5">
        <path d="M6 9V6a4 4 0 0 1 8 0v3"/>
        <rect x="2" y="9" width="16" height="11" rx="1"/>
      </svg>
      <span class="badge">2</span>
    </div>
  </header>

  <section class="hero">
    <div class="hero-panel">
      <svg width="829" height="675" viewBox="0 0 829 675">
        <polygon points="230,0 400,0 60,300 0,340 0,250" fill="#ffffff" opacity="0.04"/>
        <polygon points="0,0 150,0 0,160" fill="#ffffff" opacity="0.03"/>
        <polygon points="330,675 470,675 620,480 520,480" fill="#ffffff" opacity="0.03"/>
        <polygon points="180,675 270,675 420,470 360,470" fill="#ffffff" opacity="0.025"/>
      </svg>
      <h1 class="headline">Premium Auto Parts<br>That Keep you Moving</h1>
      <p class="lead">Lorem ipsum dolor sit amet, consectetur adipiscing elit, sed do eiusmod tempor incididunt ut labore et dolore magna aliqua. Quis ipsum suspendisse ultrices gravida</p>
      <div class="stats">
        <div class="stat"><div class="num">25</div><div class="label">FEATURE</div><div class="desc">Description</div></div>
        <div class="stat"><div class="num">10</div><div class="label">FEATURE</div><div class="desc">Description</div></div>
        <div class="stat"><div class="num">02</div><div class="label">FEATURE</div><div class="desc">Description</div></div>
      </div>
      <div class="cta">KNOW MORE</div>
    </div>
    <div class="hero-photo" role="img" aria-label="Photo of a row of turquoise and white heavy trucks parked on a lot"></div>
  </section>
</body>
</html>
```